App Design Project

We had an tavrix/vemo app built (freelancer), without any real design applied. Currently just made up of plain buttons and text. No colors, images, etc.
App is about 20 total pages, and contains a login window, a main menu, and then several different options that pull data via web services from our back-end.
About the app:
The application will be used by physicians, who are in essence speakers who are speaking on behalf of pharmaceutical companies, to train doctors on the use of their products. They will use the app to get a list of their upcoming speaking engagements, calendars, access to slide presentations, and the ability for them to submit expense forms with pictures of receipts, etc.
We need the following things:
* An App Icon
* An Tavrix startup screen
* Two Vemo startup screens (one portrait and one landscape)
* Color schedme recommendations for the pages
* Page design recommendations: header/footer
The Tavrix and Vemo startup screens are screens displayed while the app is loading (splash screen). They are simply a large version of the app's logo (with differing dimensions) and maybe some extra detail as the space allows more. The Vemo and Tavrix screens can be identical, but please note the size. orientation and aspect ratio differences.
Objects possibilities...(pick any/none/anything else that is appropriate):
* Person behind a podium
* Someone speaking / presenting
* be creative
Styles we like:
This is for pharma, so medical might be appropriate
open to recommendations
Keep in mind that we are looking for page design recommendations as well. We could provide sample screens with text, and then are looking for recommendations on color, and general page design.
A successful designer may also win several other apps currently under consideration.

```html
<!DOCTYPE html>
<html lang="en">
<head>
<meta charset="utf-8">
<title>ClinVoice – My Meetings</title>
<link rel="stylesheet" href="https://fonts.googleapis.com/css2?family=Didact+Gothic&display=swap">
<style>
  :root {
    --page-bg: #ffffff;
    --screen-bg: #070707;
    --status-bg: #000000;
    --header-bg: #161616;
    --text-light: #f4f4f4;
    --back-orange: #e8792f;
    --home-teal: #2aaacb;
    --menu-top: #4d93ea;
    --menu-bottom: #2e6fd8;
    --menu-divider: #1d4a96;
    --footer-bg: #1c1c1c;
    --footer-text: #cfcfcf;
    --link-blue: #8fb6f2;
    --brand-dot: #2a9fd0;
  }
  * { box-sizing: border-box; margin: 0; padding: 0; }
  html, body {
    width: 1200px; height: 1200px; overflow: hidden;
    background: var(--page-bg);
    font-family: "Didact Gothic", "Century Gothic", sans-serif;
  }
  .screen {
    position: absolute; left: 232px; top: 48px;
    width: 736px; height: 1104px;
    background: var(--screen-bg);
    display: flex; flex-direction: column;
    color: var(--text-light);
  }
  .status-bar {
    height: 46px; background: var(--status-bg);
    display: flex; align-items: center; padding: 0 14px;
    font-size: 24px; font-weight: bold; gap: 26px;
  }
  .status-bar .spacer { flex: 1; }
  .status-bar svg { display: block; }
  .app-header {
    height: 124px; background: var(--header-bg);
    display: flex; align-items: center; padding-left: 40px; gap: 26px;
  }
  .brand-dot {
    width: 74px; height: 74px; border-radius: 50%;
    background: var(--brand-dot);
  }
  .brand-name { font-size: 74px; letter-spacing: -1px; color: var(--text-light); }
  .page-title {
    height: 191px; display: flex; align-items: center; justify-content: center;
    font-size: 69px;
  }
  .nav-row { height: 80px; display: flex; }
  .nav-row a {
    flex: 1; display: flex; align-items: center; justify-content: center;
    font-size: 42px; color: var(--text-light); text-decoration: none;
  }
  .nav-back { background: var(--back-orange); }
  .nav-home { background: var(--home-teal); }
  .menu { display: flex; flex-direction: column; }
  .menu-item {
    height: 103.5px; display: flex; align-items: center; justify-content: center;
    font-size: 52px; color: var(--text-light); text-decoration: none;
    background: linear-gradient(to bottom, var(--menu-top), var(--menu-bottom));
    border-top: 2px solid var(--menu-divider);
  }
  .app-footer {
    flex: 1; background: var(--footer-bg);
    display: flex; flex-direction: column; align-items: center;
    padding-top: 16px; font-size: 17px; line-height: 24px;
    color: var(--footer-text); font-weight: bold; text-align: center;
  }
  .footer-links {
    display: flex; justify-content: space-around; width: 100%;
    padding: 8px 30px 0; font-size: 25px; font-weight: normal;
  }
  .footer-links a { color: var(--link-blue); }
</style>
</head>
<body>
  <main class="screen">
    <div class="status-bar">
      <svg width="40" height="20" viewBox="0 0 40 20" aria-hidden="true">
        <rect x="0" y="16" width="5" height="4" fill="#fff"/>
        <rect x="8" y="12" width="5" height="8" fill="#fff"/>
        <rect x="16" y="8" width="5" height="12" fill="#fff"/>
        <rect x="24" y="4" width="5" height="16" fill="#fff"/>
        <rect x="32" y="0" width="5" height="20" fill="#fff"/>
      </svg>
      <span>T/29</span>
      <span>3G</span>
      <span class="spacer"></span>
      <svg width="22" height="26" viewBox="0 0 22 26" aria-hidden="true">
        <path d="M5 12 V8 a6 6 0 0 1 12 0 V12" fill="none" stroke="#fff" stroke-width="3"/>
        <rect x="2" y="12" width="18" height="14" fill="#fff"/>
      </svg>
      <span class="spacer"></span>
      <svg width="52" height="24" viewBox="0 0 52 24" aria-hidden="true">
        <rect x="1.5" y="1.5" width="44" height="21" rx="3" fill="none" stroke="#fff" stroke-width="3"/>
        <rect x="5" y="5" width="37" height="14" fill="#fff"/>
        <rect x="47" y="8" width="4" height="8" fill="#fff"/>
      </svg>
    </div>

    <header class="app-header">
      <span class="brand-dot"></span>
      <span class="brand-name">ClinVoice</span>
    </header>

    <h1 class="page-title" style="font-weight:normal">My Meetings</h1>

    <nav class="nav-row">
      <a class="nav-back" href="#">Back</a>
      <a class="nav-home" href="#">Home</a>
    </nav>

    <nav class="menu">
      <a class="menu-item" href="#">Next Meetings</a>
      <a class="menu-item" href="#">Previous Meetings</a>
      <a class="menu-item" href="#">Calendar</a>
      <a class="menu-item" href="#">Action Items</a>
      <a class="menu-item" href="#">Finances</a>
    </nav>

    <footer class="app-footer">
      <p>For NVL/Castrin Internal Use and For The Use of Contracted Speakers Only</p>
      <p>Not to be shared outside CT/NVL collaborative team</p>
      <p>v11.1 Copyright @2011 Norvell Labs. All rights reserved</p>
      <div class="footer-links">
        <a href="#">Go to Full Site</a>
        <a href="#">Privacy Statement</a>
        <a href="#">Terms of Use</a>
      </div>
    </footer>
  </main>
</body>
</html>
```